Plimora

We need a design for a mobile app (Android & iOS) with the following features:
- Recommend other applications based on different criteria, such as similar applications, hot apps, apps installed by friends and so on.
- Recommend a featured app everyday.
- List installed apps on the device.
- List harmful or malicious installed apps on the device
- List hot apps according to the more used apps by the comunity or the user's friends
- Profiles: Save the list of apps installed on the device as a list to allow the user to restore them on other devices.

Industry/Entity Type

Android

Requirements
Must have
• Find attached to this project a mockup of the screen elements desired.
To put it in a nutshell, the main elements are:
- Main Menu: A main menu to access the other modules of the app

- Recommended Apps: List of apps recommended, each app will display: icon, title, price, the reason(s) why it was recommended (can be expandable if takes too much room), a button to install and a button to ignore the advice.

- Application of the day: A screen that contains the icon of the app, its rating, some screenshots, a short description or promotional text, and a button to install the app. It must be also available a way to display the history and see the recommended applications the previous days.

- Installed Apps: A list with the apps on the device. It will show the app's icon, name, package, size and a button to share the app.

- Harmful apps: List of dangerous apps found on the device. It will show the icon of the app and the name. A visual and textual indicator to measure the dangerous, and the reasons of the report. It will also includes a button to ignore the advice and another one to uninstall the application.

- Login/My account: These screens will be used to login and manage the account. The account management options are listed on the attached document.

- Profiles: The design must include the proper screens and dialogs to: save a profile, restore a profile (install the missing apps on the device), show the apps saved on the profile.

- Hot Apps: The app must allow to filter between the hot apps and the hot apps installed by the user's friends. For each app, must show: the icon, name and a trending indicator in order to say if the app is winning or losing popularity

- Miscellaneous: Other features required:
+ Login screen: The login is made in two steps. First, the user introduce their email. If the email is already registered, enters the password. Otherwise, register a new account introducing a password twice (password + repeat password, please check the attached file for more info).
+ Password recovery and password change screens
+ Loading splash (shown at the start of the application for 2-4 seconds)
+ A proper layout to inform about errors / messages in empty lists, (for example if no harmful apps where found).
+ A proper layout for loading process, for example when scanning for harmful apps.
+ Vectorial App Icon: At least one icon for the app (512 x512 px)
+ Vectorial Featured (1024x500 px) and Promo banners (180x120 px) for Vexari Shop.
+ For the UI elements like buttons or checkboxes is required the following status: normal, pressed, disabled and focused.
Nice to have
• Examples of apps with nice designs:

Trendle: https://shop.vexari.example/apps/details?id=com.trendle
Quill Digest: https://shop.vexari.example/apps/details?id=com.borvik.quill
ORB Coastal Terminals: https://tunes.halvexo.example/es/app/orb-coastal-terminals/id871402965?mt=8
Should not have
• The app should not have garish or poorly contrasted colors and icons.

```html
<!DOCTYPE html>
<html lang="en">
<head>
<meta charset="utf-8">
<title>Plimora – main menu screens</title>
<link rel="stylesheet" href="https://fonts.googleapis.com/css2?family=Jost:wght@300;400&display=swap">
<style>
  :root {
    --stage-light: #f4f4f4;
    --stage-dark: #b9b9b9;
    --teal-top: #1aa899;
    --teal-bottom: #0b8679;
    --teal-icon: #5cc2b4;
    --panel: #333333;
    --panel-edge: #4a4a4a;
    --rule-dark: #262626;
    --rule-light: #4c4c4c;
    --header-dark: #2b2b2b;
    --deep-teal-top: #242a2a;
    --deep-teal-mid: #137a70;
    --deep-teal-low: #0a6e65;
    --text: #ffffff;
    --button-frame: #d6d6d6;
    --button-dark: #2a2626;
  }
  * { box-sizing: border-box; margin: 0; padding: 0; }
  html, body { width: 1200px; height: 705px; overflow: hidden; }
  body {
    font-family: "Jost", "Futura", sans-serif;
    font-weight: 300;
    color: var(--text);
    background: radial-gradient(ellipse at 50% 45%, var(--stage-light) 0%, #dcdcdc 60%, var(--stage-dark) 100%);
    position: relative;
  }
  .screen {
    position: absolute;
    width: 376px;
    height: 640px;
    background: var(--panel);
    border: 1px solid var(--panel-edge);
  }
  .screen--one { left: 14px; top: 27px; }
  .screen--two { left: 408px; top: 27px; }
  .screen--three {
    left: 807px; top: 29px; height: 641px; width: 375px;
    background: linear-gradient(180deg, var(--deep-teal-top) 0%, #1a4a46 18%, var(--deep-teal-mid) 45%, var(--deep-teal-low) 82%, #1d2a29 100%);
    border-color: #666;
  }
  .app-bar {
    position: absolute; left: -1px; top: -1px; right: -1px; height: 47px;
    background: linear-gradient(180deg, var(--teal-top), var(--teal-bottom));
    display: flex; align-items: center; justify-content: center;
    font-size: 24px; font-weight: 400; letter-spacing: 0.3px;
  }
  .screen--three .app-bar { background: var(--header-dark); height: 48px; border-bottom: 2px solid #9a9a9a; }
  .app-bar svg { position: absolute; top: 50%; transform: translateY(-50%); width: 34px; height: 34px; }
  .app-bar .back { left: 9px; }
  .app-bar .settings { right: 10px; }
  .tagline {
    position: absolute; left: 0; right: 0; top: 68px;
    text-align: center; font-size: 17.5px; line-height: 25px; font-weight: 300;
  }
  .screen--three .tagline { top: 70px; }
  .menu { position: absolute; left: 3px; right: 3px; top: 169px; list-style: none; }
  .screen--three .menu { left: 0; right: 0; top: 159px; }
  .menu-item {
    height: 67.5px; display: flex; align-items: center;
    border-top: 1px solid var(--rule-dark);
    box-shadow: inset 0 1px 0 var(--rule-light);
    font-size: 21px; font-weight: 300;
  }
  .menu-item:last-child { border-bottom: 1px solid var(--rule-dark); box-shadow: inset 0 1px 0 var(--rule-light), 0 1px 0 var(--rule-light); }
  .screen--three .menu-item { border-top-color: #123f3b; box-shadow: inset 0 1px 0 #4f8c86; }
  .screen--three .menu-item:last-child { border-bottom-color: #123f3b; box-shadow: inset 0 1px 0 #4f8c86, 0 1px 0 #4f8c86; }
  .menu-icon { width: 90px; display: flex; justify-content: center; padding-right: 4px; }
  .menu-icon svg { width: 40px; height: 44px; }
  .account-button {
    position: absolute; left: 46px; top: 562px; width: 291px; height: 49px;
    border: 4px solid var(--button-frame); border-radius: 9px;
    background: linear-gradient(180deg, var(--teal-top), var(--teal-bottom));
    display: flex; align-items: center; justify-content: center; gap: 16px;
    font-size: 21px; font-weight: 300;
  }
  .screen--three .account-button { left: 42px; top: 552px; background: var(--button-dark); }
  .account-button svg { width: 36px; height: 32px; }
</style>
</head>
<body>

<svg width="0" height="0" style="position:absolute" aria-hidden="true">
  <defs>
    <symbol id="i-back" viewBox="0 0 34 34"><circle cx="17" cy="17" r="15" fill="none" stroke="#fff" stroke-width="2.6"/><path d="M25 17H11M16 11l-6 6 6 6" fill="none" stroke="#fff" stroke-width="2.8" stroke-linecap="round" stroke-linejoin="round"/></symbol>
    <symbol id="i-gear" viewBox="0 0 34 34"><circle cx="17" cy="17" r="15" fill="none" stroke="#fff" stroke-width="2.6"/><g fill="#fff" transform="translate(17 17)"><circle r="6.5"/><rect x="-2" y="-10" width="4" height="20"/><rect x="-2" y="-10" width="4" height="20" transform="rotate(45)"/><rect x="-2" y="-10" width="4" height="20" transform="rotate(90)"/><rect x="-2" y="-10" width="4" height="20" transform="rotate(135)"/></g><circle cx="17" cy="17" r="3" fill="#2b2b2b"/></symbol>
    <symbol id="i-ribbon" viewBox="0 0 40 44"><path d="M12 18 6 40l6-4 4 6 4-16zM28 18l6 22-6-4-4 6-4-16z" fill="#5cc2b4"/><circle cx="20" cy="13" r="11" fill="#5cc2b4"/><circle cx="20" cy="13" r="7" fill="#333"/><path d="m20 8 1.5 3.3 3.5.3-2.7 2.3.9 3.5-3.2-1.9-3.2 1.9.9-3.5-2.7-2.3 3.5-.3z" fill="#fff"/></symbol>
    <symbol id="i-calendar" viewBox="0 0 40 44"><rect x="0" y="6" width="40" height="32" fill="#5cc2b4"/><rect x="0" y="12" width="40" height="1.5" fill="#fff" opacity=".7"/><text x="20" y="34" text-anchor="middle" font-family="Jost, sans-serif" font-size="18" fill="#fff">31</text></symbol>
    <symbol id="i-download" viewBox="0 0 40 44"><path d="M7 2h18l8 8v32H7z" fill="#5cc2b4"/><path d="M25 2v8h8z" fill="#fff" opacity=".5"/><path d="M20 17v15M14 26l6 6 6-6" fill="none" stroke="#fff" stroke-width="3" stroke-linecap="round" stroke-linejoin="round"/></symbol>
    <symbol id="i-block" viewBox="0 0 40 44"><circle cx="20" cy="22" r="15" fill="none" stroke="#5cc2b4" stroke-width="4.5"/><path d="M30 12 10 32" stroke="#5cc2b4" stroke-width="4.5"/></symbol>
    <symbol id="i-star" viewBox="0 0 40 44"><path d="m20 5 4.6 10.5 11.4 1-8.6 7.5 2.6 11.2L20 29.3 10 35.2l2.6-11.2L4 16.5l11.4-1z" fill="#5cc2b4"/></symbol>
    <symbol id="i-person" viewBox="0 0 36 32"><circle cx="18" cy="9" r="7" fill="#5cc2b4"/><path d="M2 30c0-8 7-12 16-12s16 4 16 12z" fill="#5cc2b4"/><path d="M18 19l-2 4 2 7 2-7z" fill="#fff" opacity=".8"/></symbol>
  </defs>
</svg>

<section class="screen screen--one" aria-label="Main menu, signed in">
  <header class="app-bar"><svg class="back"><use href="#i-back"/></svg>Plimora<svg class="settings"><use href="#i-gear"/></svg></header>
  <p class="tagline">“Lorem ipsum dolor sit amet,<br>consectetur adipisicing elit do ”</p>
  <ul class="menu">
    <li class="menu-item"><span class="menu-icon"><svg><use href="#i-ribbon"/></svg></span>Recommended Apps</li>
    <li class="menu-item"><span class="menu-icon"><svg><use href="#i-calendar"/></svg></span>App of the day</li>
    <li class="menu-item"><span class="menu-icon"><svg><use href="#i-download"/></svg></span>Installed apps</li>
    <li class="menu-item"><span class="menu-icon"><svg><use href="#i-block"/></svg></span>Harmful apps</li>
    <li class="menu-item"><span class="menu-icon"><svg><use href="#i-star"/></svg></span>Hot apps</li>
  </ul>
  <div class="account-button"><svg><use href="#i-person"/></svg>My account</div>
</section>

<section class="screen screen--two" aria-label="Main menu, signed out">
  <header class="app-bar"><svg class="back"><use href="#i-back"/></svg>Plimora<svg class="settings"><use href="#i-gear"/></svg></header>
  <p class="tagline">“Lorem ipsum dolor sit amet,<br>consectetur adipisicing elit do ”</p>
  <ul class="menu">
    <li class="menu-item"><span class="menu-icon"><svg><use href="#i-ribbon"/></svg></span>Recommended Apps</li>
    <li class="menu-item"><span class="menu-icon"><svg><use href="#i-calendar"/></svg></span>App of the day</li>
    <li class="menu-item"><span class="menu-icon"><svg><use href="#i-download"/></svg></span>Installed apps</li>
    <li class="menu-item"><span class="menu-icon"><svg><use href="#i-block"/></svg></span>Harmful apps</li>
    <li class="menu-item"><span class="menu-icon"><svg><use href="#i-star"/></svg></span>Hot apps</li>
  </ul>
  <div class="account-button"><svg><use href="#i-person"/></svg>Login</div>
</section>

<section class="screen screen--three" aria-label="Main menu, teal theme">
  <header class="app-bar"><svg class="back"><use href="#i-back"/></svg>Plimora<svg class="settings"><use href="#i-gear"/></svg></header>
  <p class="tagline">“Lorem ipsum dolor sit amet,<br>consectetur adipisicing elit do ”</p>
  <ul class="menu">
    <li class="menu-item"><span class="menu-icon"><svg><use href="#i-ribbon"/></svg></span>Recommended Apps</li>
    <li class="menu-item"><span class="menu-icon"><svg><use href="#i-calendar"/></svg></span>App of the day</li>
    <li class="menu-item"><span class="menu-icon"><svg><use href="#i-download"/></svg></span>Installed apps</li>
    <li class="menu-item"><span class="menu-icon"><svg><use href="#i-block"/></svg></span>Harmful apps</li>
    <li class="menu-item"><span class="menu-icon"><svg><use href="#i-star"/></svg></span>Hot apps</li>
  </ul>
  <div class="account-button"><svg><use href="#i-person"/></svg>Login</div>
</section>

</body>
</html>
```